Our new all natural drink needs a product design (logo and front-pack).
We developed an innovative alternative under the brand name "Plain Sip Co" - all natural and great tasting soft drink and ice tea, beyond the conventional big commercial brands. Our ambition is to set a new high standard for soft drinks and ice tea, produced in a simple honest manner.

Target Market(s)

European markets

Colors

Designer to choose colors to be used in the design.

Requirements
Must have
• We want “clean” minimalist design with focus on the number “1”, but also to present the ingredients we have inside the different flavor variants (see the brief attached)
• We also want to be visible and easy recognizable on the shelves in-store
Nice to have
• Product benefits: 100% natural products. No white sugar, aromas, colors, additives, artificial substances, citric acids or ascorbic acids allowed.
• We focus on the highest quality possible and superior natural taste experiences. In general, no compromises!
Should not have
• Must not be overcrowded and with too much colors. Must not have similarities with the conventional big commercial brands (e.g. Fizzmora, Bruvo, etc.)

```html
<!DOCTYPE html>
<html lang="en">
<head>
<meta charset="utf-8">
<title>Plain Sip Co – Range</title>
<link rel="stylesheet" href="https://fonts.googleapis.com/css2?family=Quicksand:wght@300;400;500&display=swap">
<style>
  :root {
    --bg: #ffffff;
    --ink: #111111;
    --cap: #b9bcbd;
    --cap-dark: #8d9091;
    --glass: #eef1f1;
    --white: #ffffff;
    --fig: #c3cc3a;
    --fig-ink: #b8bf2c;
    --peach: #fbbd14;
    --peach-ink: #f2b315;
    --forest: #f7a6c5;
    --forest-ink: #ec7fa6;
    --lemon: #fcd823;
    --lemon-ink: #f0c71a;
    --pomegranate: #5e2227;
    --pomegranate-ink: #6a2a2e;
  }
  * { margin: 0; padding: 0; box-sizing: border-box; }
  html, body { width: 1200px; height: 891px; overflow: hidden; background: var(--bg); }
  body { font-family: "Quicksand", sans-serif; position: relative; }

  .range { position: absolute; inset: 0; }
  .bottle { position: absolute; top: 58px; width: 190px; height: 640px; color: var(--white); }
  .bottle-shape { position: absolute; inset: 0; }
  .bottle-shape .body { fill: var(--liquid); }

  .claim {
    position: absolute; top: 155px; left: 0; width: 190px;
    text-align: center; font-size: 13px; font-weight: 300; letter-spacing: 0.2px;
  }
  .brand {
    position: absolute; top: 280px; left: 0; width: 190px;
    text-align: center; font-size: 28px; font-weight: 300; letter-spacing: 0.5px;
  }
  .flavour {
    position: absolute; top: 444px; left: 48px; width: 94px; height: 94px;
    border-radius: 50%; background: var(--white); color: var(--label-ink);
    display: flex; flex-direction: column; align-items: center; justify-content: center;
    font-size: 11px; font-weight: 500; letter-spacing: 1.6px; line-height: 1.2; text-align: center;
  }
  .flavour .divider {
    position: relative; display: block; width: 64px; height: 0;
    border-bottom: 1.5px solid var(--label-ink); margin: 3px 0 6px;
  }
  .flavour .divider::after {
    content: ""; position: absolute; right: 0; bottom: -1.5px;
    width: 1.5px; height: 10px; background: var(--label-ink);
  }
  .flavour.compact { font-size: 9px; letter-spacing: 1px; }
  .volume {
    position: absolute; top: 584px; left: 0; width: 190px;
    text-align: center; font-size: 14px; font-weight: 300; letter-spacing: 1px;
  }

  .bottle.fig { left: 48px; --liquid: var(--fig); --label-ink: var(--fig-ink); }
  .bottle.peach { left: 275px; --liquid: var(--peach); --label-ink: var(--peach-ink); }
  .bottle.forest { left: 504px; --liquid: var(--forest); --label-ink: var(--forest-ink); }
  .bottle.lemon { left: 745px; --liquid: var(--lemon); --label-ink: var(--lemon-ink); }
  .bottle.pomegranate { left: 971px; --liquid: var(--pomegranate); --label-ink: var(--pomegranate-ink); }

  .lockup {
    position: absolute; top: 700px; left: 0; width: 1200px;
    text-align: center; color: var(--ink);
    font-size: 84px; font-weight: 300; letter-spacing: 2px;
  }
</style>
</head>
<body>
<main class="range">

  <article class="bottle fig">
    <svg class="bottle-shape" viewBox="0 0 190 640" aria-hidden="true">
      <rect x="36" y="0" width="118" height="60" rx="3" fill="var(--cap)"/>
      <rect x="36" y="52" width="118" height="8" fill="var(--cap-dark)"/>
      <rect x="40" y="60" width="110" height="22" fill="var(--glass)"/>
      <path class="body" d="M40 78 C12 92 6 120 6 170 L6 618 Q6 640 28 640 L162 640 Q184 640 184 618 L184 170 C184 120 178 92 150 78 Z"/>
    </svg>
    <p class="claim">100% Natural Ingredients</p>
    <p class="brand">Plain Sip Co</p>
    <div class="flavour"><span>Green<br>Fig</span><span class="divider"></span><span>&amp;<br>Leaves</span></div>
    <p class="volume">1.5 L</p>
  </article>

  <article class="bottle peach">
    <svg class="bottle-shape" viewBox="0 0 190 640" aria-hidden="true">
      <rect x="36" y="0" width="118" height="60" rx="3" fill="var(--cap)"/>
      <rect x="36" y="52" width="118" height="8" fill="var(--cap-dark)"/>
      <rect x="40" y="60" width="110" height="22" fill="var(--glass)"/>
      <path class="body" d="M40 78 C12 92 6 120 6 170 L6 618 Q6 640 28 640 L162 640 Q184 640 184 618 L184 170 C184 120 178 92 150 78 Z"/>
    </svg>
    <p class="claim">100% Natural Ingredients</p>
    <p class="brand">Plain Sip Co</p>
    <div class="flavour"><span>Peach<br>with</span><span class="divider"></span><span>St. John's<br>Wort</span></div>
    <p class="volume">1.5 L</p>
  </article>

  <article class="bottle forest">
    <svg class="bottle-shape" viewBox="0 0 190 640" aria-hidden="true">
      <rect x="36" y="0" width="118" height="60" rx="3" fill="var(--cap)"/>
      <rect x="36" y="52" width="118" height="8" fill="var(--cap-dark)"/>
      <rect x="40" y="60" width="110" height="22" fill="var(--glass)"/>
      <path class="body" d="M40 78 C12 92 6 120 6 170 L6 618 Q6 640 28 640 L162 640 Q184 640 184 618 L184 170 C184 120 178 92 150 78 Z"/>
    </svg>
    <p class="claim">100% Natural Ingredients</p>
    <p class="brand">Plain Sip Co</p>
    <div class="flavour"><span>Forest<br>Fruits</span><span class="divider"></span><span>with<br>Roses</span></div>
    <p class="volume">1.5 L</p>
  </article>

  <article class="bottle lemon">
    <svg class="bottle-shape" viewBox="0 0 190 640" aria-hidden="true">
      <rect x="36" y="0" width="118" height="60" rx="3" fill="var(--cap)"/>
      <rect x="36" y="52" width="118" height="8" fill="var(--cap-dark)"/>
      <rect x="40" y="60" width="110" height="22" fill="var(--glass)"/>
      <path class="body" d="M40 78 C12 92 6 120 6 170 L6 618 Q6 640 28 640 L162 640 Q184 640 184 618 L184 170 C184 120 178 92 150 78 Z"/>
    </svg>
    <p class="claim">100% Natural Ingredients</p>
    <p class="brand">Plain Sip Co</p>
    <div class="flavour"><span>Lemon<br>with</span><span class="divider"></span><span>Ironwort</span></div>
    <p class="volume">1.5 L</p>
  </article>

  <article class="bottle pomegranate">
    <svg class="bottle-shape" viewBox="0 0 190 640" aria-hidden="true">
      <rect x="36" y="0" width="118" height="60" rx="3" fill="var(--cap)"/>
      <rect x="36" y="52" width="118" height="8" fill="var(--cap-dark)"/>
      <rect x="40" y="60" width="110" height="22" fill="var(--glass)"/>
      <path class="body" d="M40 78 C12 92 6 120 6 170 L6 618 Q6 640 28 640 L162 640 Q184 640 184 618 L184 170 C184 120 178 92 150 78 Z"/>
    </svg>
    <p class="claim">100% Natural Ingredients</p>
    <p class="brand">Plain Sip Co</p>
    <div class="flavour compact"><span>Pomegranate<br>with</span><span class="divider"></span><span style="font-size:11px;letter-spacing:1.6px">Black<br>Cumin</span></div>
    <p class="volume">1.5 L</p>
  </article>

  <h1 class="lockup">Plain Sip Co</h1>
</main>
</body>
</html>
```